Building and constructions

Extension, additions, alterations, renovations, new homes, project management and supervision

Industry/Entity Type

Building

Contact Information for Business Card

Tolvane building service constructions PTY LTD
Marcus Delveno builder/ supervisor
BLD 71940 member of RHG
0412735190 email tmrk41@qelmora.com

```html
<!DOCTYPE html>
<html lang="en">
<head>
<meta charset="utf-8">
<title>Tolvane Building Service Constructions – Business Cards</title>
<link rel="stylesheet" href="https://fonts.googleapis.com/css2?family=Open+Sans:wght@400;600;700&display=swap">
<style>
  :root {
    --backdrop: #3b3430;
    --card: #1a1a1b;
    --card-edge: #252526;
    --accent: #e07a1f;
    --ink: #ffffff;
  }
  * { box-sizing: border-box; margin: 0; padding: 0; }
  html, body {
    width: 1200px;
    height: 844px;
    overflow: hidden;
    background: var(--backdrop);
    font-family: "Open Sans", Arial, sans-serif;
  }
  .canvas {
    position: relative;
    width: 1200px;
    height: 844px;
  }
  .business-card {
    position: absolute;
    top: 264px;
    width: 540px;
    height: 316px;
    background: radial-gradient(ellipse at 40% 30%, var(--card-edge), var(--card) 70%);
    box-shadow: 0 12px 32px rgba(0,0,0,0.45);
    color: var(--ink);
  }
  .card-front { left: 40px; }
  .card-back { left: 620px; }

  .brand {
    position: absolute;
    left: 0;
    right: 0;
    display: flex;
    justify-content: center;
    align-items: center;
    gap: 12px;
  }
  .card-front .brand { top: 70px; }
  .card-back .brand { top: 104px; }
  .brand-square {
    width: 50px;
    height: 50px;
    background: var(--accent);
  }
  .brand-name {
    font-weight: 700;
    font-size: 19px;
    line-height: 1.2;
    color: var(--ink);
  }

  .contact-list {
    position: absolute;
    right: 36px;
    top: 156px;
    list-style: none;
    font-size: 11.5px;
  }
  .contact-item {
    display: flex;
    justify-content: flex-end;
    align-items: center;
    gap: 8px;
    margin-bottom: 12px;
  }
  .contact-icon { width: 11px; height: 11px; fill: var(--accent); }

  .holder {
    position: absolute;
    left: 38px;
    bottom: 42px;
  }
  .holder-name {
    color: var(--accent);
    font-weight: 600;
    font-size: 16px;
    line-height: 1.2;
  }
  .holder-role {
    font-size: 12px;
    line-height: 1.4;
  }
  .registration {
    position: absolute;
    left: 232px;
    bottom: 52px;
    font-size: 11.5px;
  }
</style>
</head>
<body>
<main class="canvas">
  <section class="business-card card-front">
    <div class="brand">
      <span class="brand-square" aria-hidden="true"></span>
      <p class="brand-name">Tolvane Building Service<br>Constructions PTY LTD</p>
    </div>

    <ul class="contact-list">
      <li class="contact-item">
        <span>0412735190</span>
        <svg class="contact-icon" viewBox="0 0 24 24" aria-hidden="true"><path d="M6.6 10.8a15 15 0 0 0 6.6 6.6l2.2-2.2a1 1 0 0 1 1-.25 11.4 11.4 0 0 0 3.6.57 1 1 0 0 1 1 1V20a1 1 0 0 1-1 1A17 17 0 0 1 3 4a1 1 0 0 1 1-1h3.5a1 1 0 0 1 1 1c0 1.25.2 2.45.57 3.57a1 1 0 0 1-.25 1z"/></svg>
      </li>
      <li class="contact-item">
        <span>tmrk41@qelmora.com</span>
        <svg class="contact-icon" viewBox="0 0 24 24" aria-hidden="true"><path d="M2 5h20v14H2z"/><path d="M2 5l10 8 10-8" fill="none" stroke="#1a1a1b" stroke-width="1.8"/></svg>
      </li>
    </ul>

    <div class="holder">
      <p class="holder-name">Marcus Delveno</p>
      <p class="holder-role">Builder/ Supervisor</p>
    </div>

    <p class="registration">BLD 71940 Member of RHG</p>
  </section>

  <section class="business-card card-back">
    <div class="brand">
      <span class="brand-square" aria-hidden="true"></span>
      <p class="brand-name">Tolvane Building Service<br>Constructions PTY LTD</p>
    </div>
  </section>
</main>
</body>
</html>
```